Letter Head Design - Finance industry

Design a letterhead to match the logo. Needs to be clean, simple and crisp. I'm open to suggestions. Will be using the logo that was submitted last with the W crossed over

Target Market(s)

Small medium businesses and government department's

Industry/Entity Type

Industry

Font styles to use
Sans Serif

Colors
cadf82
bcd85c
acd036
9bcb3c
e9e9e9
aaaaaa
000000
7f7f7f
b7b7b7

Requirements
Must have
• Need to display: Logo, Business address, ABN number, ASIC register number, contact phone, website, company email. Details are as per below:

Suite 4B Level 17
Marlowe Crest House
9 Tindall Lane
Sydney NSW 2000
Landline Ph: 02 5193 4620
Ph: 1300 4719 55
Email: enquiries@coinharbourco.com.au
W: www.coinharbourco.com.au

On the footer, the details below need to be specified:
ABN: 47 381 950 623
ASIC Registration Number: 31 749218605

Should not have
• No imagery or design that is not in line with the logo

```html
<!DOCTYPE html>
<html lang="en">
<head>
<meta charset="utf-8">
<title>Coin Harbour Co – Letterhead</title>
<link rel="stylesheet" href="https://fonts.googleapis.com/css2?family=Didact+Gothic&display=swap">
<style>
  :root {
    --backdrop: #5a5053;
    --paper: #f2f2f0;
    --green: #9bcb3c;
    --green-light: #acd036;
    --ink: #000000;
    --ink-soft: #3a3a3a;
    --grey: #7f7f7f;
    --rule: #b7b7b7;
  }
  * { box-sizing: border-box; margin: 0; padding: 0; }
  html, body {
    width: 1200px;
    height: 933px;
    overflow: hidden;
    background: var(--backdrop);
    font-family: "Didact Gothic", "Century Gothic", sans-serif;
  }
  .letterhead {
    position: absolute;
    left: 290px;
    top: 28px;
    width: 620px;
    height: 877px;
    background: var(--paper);
    box-shadow: 0 18px 40px rgba(0, 0, 0, 0.35);
  }
  .brand {
    position: absolute;
    left: 44px;
    top: 44px;
    display: flex;
    align-items: center;
    gap: 10px;
  }
  .brand-dot {
    width: 30px;
    height: 30px;
    border-radius: 50%;
    background: var(--green-light);
  }
  .brand-name {
    font-size: 21px;
    color: var(--ink);
    letter-spacing: 0.3px;
  }
  .footer {
    position: absolute;
    left: 44px;
    right: 44px;
    bottom: 56px;
    text-align: right;
    color: var(--ink-soft);
    font-size: 9.5px;
    line-height: 1.55;
  }
  .footer-rule {
    height: 1px;
    background: var(--rule);
    margin-bottom: 14px;
  }
  .footer-rule.short {
    margin: 6px 0 6px auto;
    width: 62%;
    background: #d4d4d4;
  }
  .label { color: var(--green); }
  .registration {
    font-size: 8.5px;
    color: var(--grey);
  }
</style>
</head>
<body>
  <main class="letterhead">
    <header class="brand">
      <span class="brand-dot" aria-hidden="true"></span>
      <span class="brand-name">Coin Harbour Co</span>
    </header>

    <footer class="footer">
      <div class="footer-rule"></div>
      <p class="address">Suite 4B Level 17, Marlowe Crest House, 9 Tindall Lane, Sydney NSW 2000</p>
      <p class="contact">
        <span class="label">Tel:</span> 1300 4719 55 ·
        <span class="label">Email:</span> enquiries@coinharbourco.com.au ·
        <span class="label">Web:</span> www.coinharbourco.com.au
      </p>
      <div class="footer-rule short"></div>
      <p class="registration">ABN: 47 381 950 623 · ASIC Registration Number: 31 749218605</p>
    </footer>
  </main>
</body>
</html>
```